prestige web design for KELVA Finance

Hi Guys,

Looking to team up with a creative designer for another of our websites for KELVA finance.
if looking for our similar website www.brimlendco.com.au is one of our other companies. ideally working in our logo being black and white.

Please see attachments for our logo and a description
HOME
VEHICLE
EQUIPMENT
WHO WE ARE
CONTACT US

open to ideas on layout .

touch base if you have any questions.

Target Market(s)

Prestige cars and equipment -trucks earthmoving

Industry/Entity Type

finance

Coding

Coded - Design and coding required

Number of Pages Required

5+ page

Font styles to use
Sans Serif

Colors

Designer to choose colors to be used in the design.

```html
<!DOCTYPE html>
<html lang="en">
<head>
<meta charset="utf-8">
<title>KELVA Finance – Makers of Possible</title>
<link href="https://fonts.googleapis.com/css2?family=Poppins:wght@300;400;500;600&family=Roboto:wght@400&display=swap" rel="stylesheet">
<style>
  :root{
    --ink:#111111;
    --black:#000000;
    --white:#ffffff;
    --line:#555555;
    --body:#1a1a1a;
  }
  *{box-sizing:border-box;margin:0;padding:0}
  html,body{width:1200px;height:2311px;overflow:hidden;background:var(--white)}
  body{position:relative;font-family:"Poppins",sans-serif;color:var(--body)}
  .abs{position:absolute}

  /* header */
  .site-header{left:0;top:0;width:1200px;height:74px;background:var(--white)}
  .brand{font-family:"Poppins",sans-serif;font-weight:600;letter-spacing:.5px;white-space:nowrap}
  .site-header .brand{left:161px;top:18px;font-size:28px;color:var(--black)}
  .main-nav a{position:absolute;top:29px;font-family:"Roboto",sans-serif;font-size:14.5px;color:var(--black);text-decoration:none}
  .pill{position:absolute;display:flex;align-items:center;justify-content:center;border-radius:24px;background:var(--black);color:var(--white);font-family:"Roboto",sans-serif;font-size:14.5px}
  .header-cta{left:915px;top:16px;width:124px;height:41px}

  /* hero */
  .hero-backdrop{left:0;top:74px;width:1200px;height:451px;background:linear-gradient(180deg,#4a4d52 0%,#2e3034 55%,#3b3c3f 100%)}
  .hero-title{left:0;top:116px;width:1200px;text-align:center;font-size:46px;font-weight:400;color:var(--white);line-height:1.2}
  .hero-cta{left:538px;top:192px;width:124px;height:40px;border:1px solid #888}
  .hero-fleet{left:81px;top:256px;width:1031px;height:318px;border-radius:60px 60px 30px 30px;background:linear-gradient(90deg,#d9a21c 0%,#c08a16 28%,#1b1b1d 38%,#2a2a2c 62%,#2c8170 72%,#1f6b5c 100%);opacity:.95}

  /* about */
  .about{left:0;top:622px;width:1200px;height:432px;background:var(--ink)}
  .about h2{position:absolute;left:0;top:32px;width:1200px;text-align:center;font-size:34px;font-weight:600;color:var(--white);letter-spacing:.5px}
  .about p{position:absolute;left:210px;top:100px;width:780px;text-align:center;font-size:14.4px;line-height:20.2px;color:var(--white)}
  .btn-outline{position:absolute;display:flex;align-items:center;justify-content:center;font-size:14px;font-weight:500;border:1px solid var(--black);color:var(--black);background:transparent}
  .about .btn-outline{left:542px;top:247px;width:116px;height:39px;border-color:var(--white);color:var(--white)}
  .divider{left:599px;top:1016px;width:1.5px;height:76px;background:var(--black)}

  /* why */
  .why-title{left:0;top:1113px;width:1200px;text-align:center;font-size:35px;font-weight:600;color:var(--black)}
  .why-intro{left:250px;top:1183px;width:690px;text-align:center;font-size:16px;line-height:22.5px;color:var(--black)}
  .service h3{position:absolute;font-size:26px;font-weight:500;color:var(--black)}
  .service .lead{position:absolute;font-size:17.8px;line-height:24.8px;color:var(--black);letter-spacing:.2px}
  .service .detail{position:absolute;font-size:13.9px;line-height:20.2px;color:var(--body)}
  .photo-frame{position:absolute;border:1px solid #333}
  .photo{position:absolute}
  .photo-car{left:685px;top:1266px;width:338px;height:299px;background:linear-gradient(160deg,#3a3430 0%,#6b5448 35%,#d8412a 60%,#7a6a62 100%)}
  .photo-digger{left:177px;top:1620px;width:337px;height:300px;background:linear-gradient(180deg,#6f9ed4 0%,#b9cfe2 38%,#d7a32c 58%,#b58c5a 100%)}

  /* footer */
  .site-footer{left:0;top:2041px;width:1200px;height:270px;background:var(--black);color:var(--white)}
  .site-footer .brand{position:absolute;left:0;top:29px;width:1200px;text-align:center;font-size:32px;color:var(--white)}
  .footer-nav a{position:absolute;top:104px;font-size:13.5px;color:var(--white);text-decoration:none;letter-spacing:.3px}
  .footer-nav .current{font-weight:600}
  .footer-nav .box{top:92px;left:775px;width:117px;height:39px;border:1px solid var(--white);display:flex;align-items:center;justify-content:center}
  .rule{position:absolute;left:160px;width:878px;height:1px;background:var(--line)}
  .contact-item{position:absolute;top:161px;display:flex;gap:10px;align-items:center}
  .icon-box{width:37px;height:37px;border:1px solid #999;display:flex;align-items:center;justify-content:center;flex:none}
  .contact-item p{font-size:13.6px;line-height:21px}
  .copyright{position:absolute;left:158px;top:228px;font-size:13.5px}
  .social{position:absolute;top:222px;width:37px;height:37px;border:1px solid #999}
</style>
</head>
<body>

<header class="abs site-header">
  <div class="abs brand">KELVA Finance</div>
  <nav class="main-nav">
    <a style="left:524px">HOME</a>
    <a style="left:596px">VEHICLE</a>
    <a style="left:684px">EQUIPMENT</a>
    <a style="left:796px">WHO WE ARE</a>
  </nav>
  <a class="pill header-cta">CONTACT US</a>
</header>

<section>
  <div class="abs hero-backdrop" role="img" aria-label="City skyline of tall office towers behind the vehicles"></div>
  <h1 class="abs hero-title">KELVA Finance - Makers of Possible</h1>
  <a class="pill hero-cta">CONTACT US</a>
  <div class="abs hero-fleet" role="img" aria-label="Yellow backhoe loader, black prestige sedan and green box truck lined up side by side"></div>
</section>

<section class="abs about">
  <h2>MAKERS OF POSSIBLE</h2>
  <p>KELVA Finance has nearly 20 years industry experience, so we certainly understand personal and business lending.We are committed to providing individuals and businesses with tailored financial services that enable them to reach and then exceed their financial goals.We have a vast list of lenders to suit along with an online team ready to help you, so we're easily accessible and here when you need us. Our friendly team of experienced and approachable staff that will listen, understand your situation and lend responsibly.</p>
  <a class="btn-outline">Learn More</a>
</section>
<div class="abs divider"></div>

<section>
  <h2 class="abs why-title">WHY CHOOSE US?</h2>
  <p class="abs why-intro">Well, because we're here to help you! We care about outcomes AND helping you achieve a stress and enjoyable lending experience.</p>

  <article class="service">
    <h3 style="left:162px;top:1262px">Vehicle Loan</h3>
    <p class="lead" style="left:162px;top:1323px;width:450px">While you focus on getting the right car, we will focus on getting you the right finance.</p>
    <p class="detail" style="left:162px;top:1395px;width:445px">Whether you're interested in purchasing a used or new car for yourself or a fleet of vehicles through your business, KELVA's teamare well equipped to help you find the car finance that's right for you.</p>
    <a class="btn-outline" style="left:161px;top:1502px;width:117px;height:39px">Apply Now</a>
    <div class="photo-frame" style="left:700px;top:1283px;width:338px;height:299px"></div>
    <div class="photo photo-car" role="img" aria-label="Red sports car parked in a showroom lot"></div>
  </article>

  <article class="service">
    <div class="photo-frame" style="left:161px;top:1635px;width:339px;height:301px"></div>
    <div class="photo photo-digger" role="img" aria-label="Yellow excavators on a dirt work site under a blue sky"></div>
    <h3 style="left:584px;top:1612px">Equipment</h3>
    <p class="lead" style="left:584px;top:1671px;width:450px">At KELVA, we help businesses of all sizes to secure funding in the form of a business loan for asset purchases from either a bank or private lender.</p>
    <p class="detail" style="left:584px;top:1760px;width:445px">Our dedicated Equipment Finance specialists have extensive industry experience across the agricultural, construction and earthmoving sectors. We'll work with you to understand the specific needs that face your business to keep your equipment up to date..</p>
    <a class="btn-outline" style="left:582px;top:1885px;width:117px;height:39px">Apply Now</a>
  </article>
</section>

<footer class="abs site-footer">
  <div class="brand">KELVA Finance</div>
  <nav class="footer-nav">
    <a class="current" style="left:307px">HOME</a>
    <a style="left:400px">VEHICLE</a>
    <a style="left:509px">EQUIPMENT</a>
    <a style="left:633px">WHO WE ARE</a>
    <a class="box">CONTACT US</a>
  </nav>
  <div class="rule" style="top:147px"></div>
  <div class="contact-item" style="left:161px">
    <div class="icon-box"><svg width="18" height="22" viewBox="0 0 18 22" fill="none" stroke="#fff" stroke-width="1.3"><path d="M9 21s7-7.5 7-12.5A7 7 0 0 0 2 8.5C2 13.5 9 21 9 21z"/><circle cx="9" cy="8.5" r="2.5"/></svg></div>
    <p>Company Address<br>123 company add State 123456</p>
  </div>
  <div class="contact-item" style="left:524px">
    <div class="icon-box"><svg width="20" height="20" viewBox="0 0 20 20" fill="none" stroke="#fff" stroke-width="1.3"><path d="M4 2l3 1 1 4-2 1.5a10 10 0 0 0 5.5 5.5L13 12l4 1 1 3-2 2C9 18 2 11 2 4z"/></svg></div>
    <p>Phone Number<br>123 456 7890</p>
  </div>
  <div class="contact-item" style="left:786px">
    <div class="icon-box"><svg width="22" height="16" viewBox="0 0 22 16" fill="none" stroke="#fff" stroke-width="1.3"><rect x="1" y="1" width="20" height="14"/><path d="M1 1l10 8 10-8"/></svg></div>
    <p>Email Address<br>company@kelvamail.com</p>
  </div>
  <div class="rule" style="top:208px"></div>
  <p class="copyright">Copyright © 2022 Kelva Finance. All Rights Reserved.</p>
  <a class="social" style="left:879px" aria-label="Social profile"></a>
  <a class="social" style="left:936px" aria-label="Social profile"></a>
  <a class="social" style="left:993px" aria-label="Social profile"></a>
</footer>

</body>
</html>
```